Home Health Care Agency Needs a Website (Seeking a PSD)

We need a user friendly website for a Home Health Care Agency. Our service is for the elderly and disabled. Frequently the busy professional middle-aged married daughter will use the website to arrange in-home care for an aging parent. Therefore, our website is primarily geared towards middle-aged women. In-home care is typically 24 hours a day so, a feeling of trustworthiness and security should be effectively conveyed. (Seeking a PSD- however, if you also offer coding, please let us know the cost.)

Target Market(s)

Frequently the busy professional middle-aged married daughter (possibly out of state) will use the website to arrange in-home care for an aging parent.

Industry/Entity Type

Security

Requirements
Must have
• Website must be clean, uncluttered and professional. The following menu pages are requested: Home, About Us, Services, Resources, FAQ, Employment & Contact.
Should not have
• Must not be too whimsical.

```html
<!DOCTYPE html>
<html lang="en">
<head>
<meta charset="utf-8">
<title>Harbor Home Health</title>
<link href="https://fonts.googleapis.com/css2?family=Open+Sans:ital,wght@0,400;0,600;0,700;1,400&family=Lora:wght@400&display=swap" rel="stylesheet">
<style>
:root{
  --blue:#35b6e4;
  --blue-dark:#1f9fd0;
  --pink:#e8336b;
  --ink:#3d3d3d;
  --grey-text:#8a8a8a;
  --footer-bg:#e3e3e3;
  --panel:#74757d;
  --white:#ffffff;
  --navy:#1c4f8a;
  --skin:#d9b49c;
  --hair:#6b4a38;
  --silver:#c9c6c2;
  --cardigan:#2f7fb8;
}
*{margin:0;padding:0;box-sizing:border-box}
html,body{width:759px;height:1200px;overflow:hidden;background:var(--white)}
body{font-family:"Open Sans",Arial,sans-serif;color:var(--ink)}
.page{position:relative;width:800px;height:1265px;transform:scale(0.94875);transform-origin:0 0}
.abs{position:absolute}

/* header */
.nav-bar{left:0;top:60px;width:800px;height:30px;background:linear-gradient(#5ccbef,#2eaedc)}
.nav-item{top:72px;color:var(--white);font-size:8.5px;font-weight:700;letter-spacing:.2px;white-space:nowrap}
.brand-box{left:108px;top:0;width:150px;height:105px;background:var(--white);box-shadow:0 2px 6px rgba(0,0,0,.35);z-index:3;display:flex;align-items:center;justify-content:center;gap:6px}
.brand-dot{width:14px;height:14px;border-radius:50%;background:var(--blue);flex:none}
.brand-name{font-weight:700;color:var(--blue);font-size:19px;line-height:1.05}
.call-label{left:509px;top:22px;font-size:6.5px;color:var(--grey-text)}
.call-number{left:509px;top:28px;font-size:14px;color:var(--pink);letter-spacing:.5px}
.social-dot{top:27px;width:16px;height:16px;border-radius:50%;background:var(--navy)}

/* hero */
.hero-photo{left:0;top:90px;width:800px;height:413px;
  background:
    radial-gradient(ellipse 170px 150px at 270px 200px,rgba(226,190,166,.95),rgba(226,190,166,0) 100%),
    radial-gradient(ellipse 200px 120px at 210px 110px,rgba(107,74,56,.9),rgba(107,74,56,0) 100%),
    radial-gradient(ellipse 150px 170px at 610px 230px,rgba(214,180,160,.95),rgba(214,180,160,0) 100%),
    radial-gradient(ellipse 190px 130px at 650px 120px,rgba(205,202,198,.95),rgba(205,202,198,0) 100%),
    radial-gradient(ellipse 230px 120px at 640px 390px,rgba(47,127,184,.9),rgba(47,127,184,0) 100%),
    linear-gradient(100deg,#a7a6a8 0%,#e9e6e1 45%,#dcd7d0 60%,#9a9aa2 100%)}
.hero-band{left:0;top:265px;width:440px;height:85px;background:rgba(41,170,220,.82);color:var(--white);font-size:16.5px;line-height:22px;padding:20px 0 0 124px}
.hero-band b{font-weight:700}
.quote-band{left:0;top:396px;width:800px;height:107px;background:rgba(55,185,232,.88)}
.quote{top:413px;width:126px;color:var(--white);font-size:8.5px;line-height:12px;font-style:italic}
.avatar{width:44px;height:44px;border-radius:50%;background:radial-gradient(circle at 50% 60%,#d2a68c,#7a5642);border:2px solid rgba(255,255,255,.6)}
.quote-name{font-size:8px;font-weight:700;color:var(--white);width:80px;text-align:center}
.quote-place{font-size:6.5px;font-weight:600;color:#2a8ab5;width:80px;text-align:center}

/* content */
.team-photo{left:108px;top:532px;width:184px;height:102px;
  background:
    radial-gradient(ellipse 60px 50px at 60px 90px,rgba(47,127,184,.85),rgba(47,127,184,0)),
    radial-gradient(ellipse 60px 50px at 140px 90px,rgba(255,255,255,.9),rgba(255,255,255,0)),
    linear-gradient(#cfe8f4,#7fbcd9)}
.about-title{left:307px;top:536px;font-family:"Lora",Georgia,serif;font-size:17px;color:#444;font-weight:400}
.about-text{left:307px;top:563px;width:387px;font-family:"Lora",Georgia,serif;font-size:8.5px;line-height:12.2px;color:#555}
.card-title{top:656px;width:183px;text-align:center;font-family:"Lora",Georgia,serif;font-size:12.5px;color:#444;font-weight:400}
.card-photo{top:677px;width:183px;height:70px}
.card-text{top:760px;width:183px;font-family:"Lora",Georgia,serif;font-size:8.1px;line-height:12.2px;color:#555;letter-spacing:-.05px}
.read-more{top:829px;font-family:"Lora",Georgia,serif;font-size:6.5px;color:var(--pink);letter-spacing:.3px}

/* footer */
.footer{left:0;top:880px;width:800px;height:340px;background:var(--footer-bg)}
.footer-brand{left:108px;top:920px;display:flex;align-items:center;gap:6px}
.footer-heading{font-size:10px;color:#7a7a7a;letter-spacing:.3px}
.footer-text{font-size:6px;line-height:10px;color:#888;width:110px}
.contact-row{font-size:6.5px;color:#888;display:flex;align-items:center;gap:10px}
.newsletter{left:547px;top:915px;width:150px;height:100px;background:var(--panel)}
.newsletter-head{position:absolute;left:10px;top:9px;display:flex;align-items:center;gap:7px;color:var(--white);font-size:6.5px;font-weight:600;letter-spacing:.2px}
.newsletter-input{position:absolute;left:10px;top:37px;width:130px;height:20px;background:#e6e6ea;font-size:8px;color:#666;padding:5px 7px}
.newsletter-button{position:absolute;left:10px;top:67px;width:67px;height:20px;background:var(--blue);color:var(--white);font-size:8px;text-align:center;line-height:20px}
.divider{left:110px;top:1038px;width:587px;height:1px;background:#cfcfcf}
.link-list{list-style:none;font-size:6.3px;line-height:12px;color:var(--blue-dark)}
.link-list li::before{content:"";display:inline-block;border-left:3px solid #888;border-top:2.5px solid transparent;border-bottom:2.5px solid transparent;margin-right:5px;vertical-align:0}
.bottom-bar{left:0;top:1220px;width:800px;height:45px;background:var(--blue)}
.bottom-text{top:1238px;font-size:5.8px;color:#1e5f80}
</style>
</head>
<body>
<div class="page">

  <!-- header -->
  <div class="abs nav-bar"></div>
  <div class="abs brand-box"><span class="brand-dot"></span><span class="brand-name">Harbor<br>Home<br>Health</span></div>
  <div class="abs call-label">&#9990; CALL US NOW TOLL FREE</div>
  <div class="abs call-number">1800.555.019</div>
  <div class="abs social-dot" style="left:619px"></div>
  <div class="abs social-dot" style="left:643px;background:#2aa7e0"></div>
  <div class="abs social-dot" style="left:667px"></div>
  <div class="abs nav-item" style="left:292px">HOME</div>
  <div class="abs nav-item" style="left:341px">ABOUT US</div>
  <div class="abs nav-item" style="left:409px">SERVICES</div>
  <div class="abs nav-item" style="left:475px">RESOURCES</div>
  <div class="abs nav-item" style="left:550px">FAQ</div>
  <div class="abs nav-item" style="left:591px">EMPLOYMENT &amp; CONTACT</div>

  <!-- hero -->
  <div class="abs hero-photo" role="img" aria-label="Smiling caregiver sitting face to face with an elderly woman at home"></div>
  <div class="abs hero-band"><b>Quality care</b> and <b>companionship</b> in<br>the comfort of your own home...</div>
  <div class="abs quote-band"></div>
  <p class="abs quote" style="left:190px">"Lorem ipsum dolor sit amet, consectetur adipisicing elit, sed do eiusmod tempor incididunt ut labore et dolore magna aliqua.</p>
  <div class="abs avatar" role="img" aria-label="Portrait of client Martin Cole" style="left:323px;top:417px"></div>
  <div class="abs quote-name" style="left:305px;top:467px">Martin Cole</div>
  <div class="abs quote-place" style="left:305px;top:478px">Lakeview, TX</div>
  <p class="abs quote" style="left:417px">"Lorem ipsum dolor sit amet, consectetur adipisicing elit, sed do eiusmod tempor incididunt ut labore et dolore magna aliqua.</p>
  <div class="abs avatar" role="img" aria-label="Portrait of client Ruth Ellis" style="left:551px;top:417px"></div>
  <div class="abs quote-name" style="left:533px;top:467px">Ruth Ellis</div>
  <div class="abs quote-place" style="left:533px;top:478px">Lakeview, TX</div>

  <!-- about -->
  <div class="abs team-photo" role="img" aria-label="Group of nurses and doctors in scrubs"></div>
  <h1 class="abs about-title">About Harbor Home Health</h1>
  <p class="abs about-text">Lorem ipsum dolor sit amet, consectetur adipisicing elit, sed do eiusmod tempor incididunt ut labore et dolore magna aliqua. Ut enim ad minim veniam, quis nostrud exercitation ullamco laboris nisi ut aliquip ex ea commodo consequat. Duis aute irure dolor in reprehenderit in voluptate velit esse cillum dolore eu fugiat nulla pariatur. Excepteur sint occaecat cupidatat non proident, sunt in culpa qui officia deserunt mollit anim id est laborum.</p>

  <!-- cards -->
  <h2 class="abs card-title" style="left:109px">Our Services</h2>
  <div class="abs card-photo" role="img" aria-label="Caregiver embracing an elderly woman" style="left:109px;background:radial-gradient(ellipse 50px 40px at 70px 30px,rgba(217,180,156,.9),rgba(217,180,156,0)),radial-gradient(ellipse 60px 40px at 130px 60px,rgba(47,150,184,.9),rgba(47,150,184,0)),linear-gradient(90deg,#c9c3bd,#7a6a60)"></div>
  <p class="abs card-text" style="left:109px">Lorem ipsum dolor sit amet, consectetur adipisicing elit, sed do eiusmod tempor incididunt ut labore et dolore magna aliqua. Ut enim ad minim veniam, quis nostrud exercitation ullamco</p>
  <div class="abs read-more" style="left:109px">READ MORE</div>

  <h2 class="abs card-title" style="left:309px">FAQ</h2>
  <div class="abs card-photo" role="img" aria-label="Nurse helping an elderly woman" style="left:309px;background:radial-gradient(ellipse 50px 40px at 40px 55px,rgba(47,127,184,.9),rgba(47,127,184,0)),radial-gradient(ellipse 50px 40px at 130px 30px,rgba(217,180,156,.9),rgba(217,180,156,0)),linear-gradient(90deg,#d8d4cf,#f1eeea)"></div>
  <p class="abs card-text" style="left:309px">Lorem ipsum dolor sit amet, consectetur adipisicing elit, sed do eiusmod tempor incididunt ut labore et dolore magna aliqua. Ut enim ad minim veniam, quis nostrud exercitation ullamco</p>
  <div class="abs read-more" style="left:309px">READ MORE</div>

  <h2 class="abs card-title" style="left:509px">Employment &amp; Contract</h2>
  <div class="abs card-photo" role="img" aria-label="Smiling medical staff team" style="left:509px;background:radial-gradient(ellipse 40px 35px at 65px 25px,rgba(200,150,110,.7),rgba(200,150,110,0)),radial-gradient(ellipse 45px 30px at 70px 62px,rgba(255,255,255,1),rgba(255,255,255,0)),linear-gradient(90deg,#eef2f4,#d9e3e8)"></div>
  <p class="abs card-text" style="left:509px">Lorem ipsum dolor sit amet, consectetur adipisicing elit, sed do eiusmod tempor incididunt ut labore et dolore magna aliqua. Ut enim ad minim veniam, quis nostrud exercitation ullamco</p>
  <div class="abs read-more" style="left:509px">READ MORE</div>

  <!-- footer -->
  <div class="abs footer"></div>
  <div class="abs footer-brand"><span class="brand-dot"></span><span class="brand-name" style="font-size:21px">Harbor<br>Home<br>Health</span></div>

  <div class="abs footer-heading" style="left:246px;top:915px">ABOUT</div>
  <p class="abs footer-text" style="left:246px;top:937px">There are many variations of passages of Lorem Ipsum available.</p>
  <p class="abs footer-text" style="left:246px;top:967px">There are many variations of passages of Lorem Ipsum available, but the majority have suffered alteration.</p>

  <div class="abs footer-heading" style="left:396px;top:915px">CONTACT</div>
  <p class="abs footer-text" style="left:398px;top:937px">There are many variations of passages of Lorem Ipsum available, but the majority have suffered alteration.</p>
  <div class="abs contact-row" style="left:399px;top:976px">
    <svg width="8" height="10" viewBox="0 0 8 10"><path d="M4 0a4 4 0 0 0-4 4c0 3 4 6 4 6s4-3 4-6a4 4 0 0 0-4-4zm0 5.5a1.5 1.5 0 1 1 0-3 1.5 1.5 0 0 1 0 3z" fill="#777"/></svg>Riverside</div>
  <div class="abs contact-row" style="left:398px;top:991px">
    <svg width="10" height="8" viewBox="0 0 10 8"><rect width="10" height="8" fill="#777"/><path d="M0 0l5 4 5-4" stroke="#e3e3e3" fill="none"/></svg>info@harborcare.example</div>
  <div class="abs contact-row" style="left:399px;top:1006px">
    <svg width="9" height="9" viewBox="0 0 9 9"><path d="M1 0h2l1 2-1.2 1a5 5 0 0 0 3.2 3.2L7 5l2 1v2a1 1 0 0 1-1 1A8 8 0 0 1 0 1a1 1 0 0 1 1-1z" fill="#777"/></svg>890-55501-23456</div>

  <div class="abs newsletter">
    <div class="newsletter-head"><svg width="11" height="8" viewBox="0 0 11 8"><rect x=".5" y=".5" width="10" height="7" fill="none" stroke="#fff"/><path d="M.5.5l5 4 5-4" stroke="#fff" fill="none"/></svg>SUBSCRIBE TO OUR NEWSLETTER</div>
    <div class="newsletter-input">Enter your email address</div>
    <div class="newsletter-button">SUBSCRIBE</div>
  </div>

  <div class="abs divider"></div>

  <div class="abs footer-heading" style="left:111px;top:1066px">SITE LINKS</div>
  <ul class="abs link-list" style="left:111px;top:1086px">
    <li>Home</li><li>About Us</li><li>Services</li><li>Resources</li><li>FAQ</li><li>Employment &amp; Contact.</li>
  </ul>
  <div class="abs footer-heading" style="left:262px;top:1066px">OUR CARE</div>
  <ul class="abs link-list" style="left:262px;top:1086px">
    <li>Care Services</li><li>Medical conditions</li><li>Care Scenarios</li><li>Care Services</li><li>Medical conditions</li><li>Care Scenarios</li>
  </ul>
  <ul class="abs link-list" style="left:396px;top:1086px">
    <li>Care Services</li><li>Medical conditions</li><li>Care Scenarios</li><li>Care Services</li><li>Medical conditions</li><li>Care Scenarios</li>
  </ul>
  <div class="abs footer-heading" style="left:547px;top:1066px">SOCIAL</div>

  <div class="abs bottom-bar"></div>
  <div class="abs bottom-text" style="left:111px">Copyright 2006 - 2013 © UpCount - All Rights Reserved - Business Inquiries | Feedback | Privacy | Tell a Friend</div>
  <div class="abs bottom-text" style="left:542px;top:1236px">24 Hour Page Tracker: 1,204,316 • 38.104.12.60</div>

</div>
</body>
</html>
```